Designing HTML Email Creative

Hi There,
The goal of this project is to design an HTML Email Creative.
Target Market: Minority Women 25 - 45. Low Household incomes. Stay at home moms. Middle America
Subject of Email Campaign: Top 5 Reasons To Go Back to College
The goal is to make the users Buy the top 5 reasons to go back to school and then Get Matched to Online & Local Colleges.
Call to action: Get Matched to Online & Local Colleges
You can add two buttons, one above the reasons and one below. The text in the button should be: Get Matched to Online & Local Colleges Now!
Your goal is to make the call to action in the email pop out so that users know very easily where to click to visit our site.
Please find attached the copy that is to be used in the creative.
Also, the information needs to be sourced so you can create very small links in the bottom of the email.
Also, we just need the psd file for this. Does not need to be coded.
Also, you can find some successful email creative attached so you have an idea.
Updates
Please note that we have updated the word doc with the correct content.
Target Market(s)
Women 25 - 50 - Low Household Incomes - Middle America
Industry/Entity Type
School
Look and feel

```html
<!DOCTYPE html>
<html lang="en">
<head>
<meta charset="utf-8">
<title>Top 5 Reasons To Go Back to College</title>
<link rel="stylesheet" href="https://fonts.googleapis.com/css2?family=Montserrat:wght@400;500;600;700&family=Raleway:wght@400;500&display=swap">
<style>
  :root {
    --orange: #f7941d;
    --button: #fbb040;
    --button-shadow: rgba(0,0,0,0.28);
    --ink: #222222;
    --muted: #555555;
    --frame: #9a9a9a;
    --paper: #ffffff;
  }
  * { box-sizing: border-box; margin: 0; padding: 0; }
  html, body { width: 783px; height: 1200px; overflow: hidden; background: var(--paper); }
  body { position: relative; font-family: "Raleway", Arial, sans-serif; color: var(--ink); }

  .email-frame {
    position: absolute; left: 0; top: 0; width: 783px; height: 1044px;
    border: 1px solid var(--frame); border-bottom: 1.5px solid #444;
  }
  .headline {
    position: absolute; top: 12px; left: 0; width: 100%; text-align: center;
    font-family: "Montserrat", sans-serif; font-weight: 700; font-size: 46px; line-height: 56px;
    color: var(--orange); letter-spacing: -0.5px;
  }
  .intro {
    position: absolute; top: 67px; left: 0; width: 100%; text-align: center;
    font-size: 19px; line-height: 24px; color: var(--ink); font-weight: 500;
  }
  .cta {
    position: absolute; left: 74px; width: 643px; height: 72px;
    display: flex; align-items: center; justify-content: center;
    background: var(--button); border-radius: 36px;
    box-shadow: 3px 4px 5px var(--button-shadow);
    font-family: "Montserrat", sans-serif; font-weight: 600; font-size: 24px;
    color: var(--ink); text-decoration: none;
  }
  .cta-top { top: 144px; }
  .cta-bottom { top: 864px; }

  .reasons {
    position: absolute; top: 248px; left: 74px; width: 643px; height: 577px;
    border: 8px solid var(--button); border-radius: 46px;
  }
  .reason { position: absolute; left: 74px; width: 479px; text-align: center; }
  .reason-1 { top: 22px; }
  .reason-2 { top: 138px; }
  .reason-3 { top: 292px; }
  .reason-4 { top: 382px; }
  .reason-5 { top: 472px; }
  .reason h2 {
    font-family: "Montserrat", sans-serif; font-weight: 600; font-size: 18.5px;
    line-height: 24px; color: var(--ink);
  }
  .reason p {
    font-size: 14.3px; line-height: 19.5px; color: var(--ink); font-weight: 500;
    text-align: justify; text-align-last: center;
  }
  .reason sup, .sources sup { color: var(--orange); font-size: 8px; }

  .closing { position: absolute; top: 954px; left: 0; width: 100%; text-align: center; }
  .closing strong { display: block; font-family: "Montserrat", sans-serif; font-weight: 600; font-size: 19px; line-height: 27px; }
  .closing span { display: block; font-size: 18.5px; line-height: 27px; font-weight: 500; }

  .sources {
    position: absolute; top: 1056px; left: 14px; width: 760px;
    list-style: none; font-size: 8px; line-height: 10.5px; color: var(--muted);
  }
  .sources li { margin-bottom: 6px; }
  .sources a { color: var(--orange); text-decoration: none; }
</style>
</head>
<body>
  <div class="email-frame">
    <h1 class="headline">Empower yourself!</h1>
    <p class="intro">Education frees you financially and boosts your<br>self-esteem and self-confidence.</p>

    <a class="cta cta-top" href="#">Get Matched to Online &amp; Local Colleges Now</a>

    <section class="reasons">
      <div class="reason reason-1">
        <h2>Education Pays - Make Double the Money</h2>
        <p>College grads earn nearly twice as much as those with only high school diplomas. Median weekly salary with high school diploma, $652. Median weekly salary with Bachelor's degree $1,066.<sup>i</sup></p>
      </div>
      <div class="reason reason-2">
        <h2>Government Grants - Federal Access Grants</h2>
        <p>College is more affordable than you think. Federal Access Grants of up to $5,550 are available to qualifying students. Grants are free money, which does not have to be paid back. Other Federal and state grants are also available, as are low cost government loans and countless scholarships.<sup>ii</sup></p>
      </div>
      <div class="reason reason-3">
        <h2>Lower Unemployment Rates for College Grads</h2>
        <p>High school graduates 8.3% unemployed, college graduates 4.5 % unemployed.<sup>iii</sup></p>
      </div>
      <div class="reason reason-4">
        <h2>Make $1 Million More in your Lifetime</h2>
        <p>On average, those with a bachelor's degree earn a $1 million more in their lifetime than those with a high school diploma.<sup>iv</sup></p>
      </div>
      <div class="reason reason-5">
        <h2>Be More Employable</h2>
        <p>Of the 2 million plus job added during the recent U.S. economic recovery, the majorities were for college graduates.<sup>v</sup></p>
      </div>
    </section>

    <a class="cta cta-bottom" href="#">Get Matched to Online &amp; Local Colleges Now</a>

    <div class="closing">
      <strong>You with a college degree — oh, the places you will go.</strong>
      <span>Click here to explore the possibilities.</span>
    </div>
  </div>

  <ol class="sources">
    <li><sup>i.</sup>"Education Pays," Northfield Labor Research Office, January 28 2013. Accessed April 21, 2013<br>&lt;<a href="#">http://www.northfieldlabor.example/earnings-chart</a>&gt;</li>
    <li><sup>ii.</sup>"Access Grants" Student Aid Desk, Brightway Education Office. Accessed April 21, 2013<br>&lt;<a href="#">http://brightwayaid.example/grants</a>&gt;</li>
    <li><sup>iii.</sup>"Education Pays," Northfield Labor Research Office, January 28 2013. Accessed April 21, 2013<br>&lt;<a href="#">http://www.northfieldlabor.example/earnings-chart</a>&gt;</li>
    <li><sup>iv.</sup>Meridian Population Survey, October 2012. Accessed April 20, 2013. &lt;<a href="#">http://meridiansurvey.example/2012/report-04.pdf</a>&gt;</li>
    <li><sup>v.</sup>Harlow, Janine. "What is a College Education Worth?" Mindful Living Weekly, August 16 2012. Accessed April 20, 2013.<br>&lt;<a href="#">http://mindfullivingweekly.example/blog/what-is-college-worth</a>&gt;</li>
  </ol>
</body>
</html>
```